CV Template

We need a graphic design to our new CV templates for our consultants. We are a small young Danish upcoming IT-business company making software solutions for our customers etc. You can visit our new website here: dev.solbakken-data.com, then you can see our web design, colors etc. I have attached a file for your inspiration :-) In the presentation I would like to have a picture of the employee, some text who descripe the profile/consultant and then I imagine that there is a table where we can write the employee's skills etc.

I would like the design to be "fresh & catchy" :-)

Looking forward to hear from you.

Best regards,
Birgit

```html
<!DOCTYPE html>
<html lang="en">
<head>
<meta charset="utf-8">
<title>CV Template – Solbakken Data</title>
<link href="https://fonts.googleapis.com/css2?family=Fira+Sans+Condensed:ital,wght@0,400;0,600;1,400&family=Open+Sans:ital,wght@0,400;0,700;1,400&display=swap" rel="stylesheet">
<style>
  :root {
    --orange: #f27e22;
    --orange-dark: #a9581a;
    --navy: #1f4c6b;
    --footer: #244f6a;
    --text: #333333;
    --grey-line: #e3e3e3;
    --dot-empty: #d0d0d0;
    --photo: #b4b7bb;
    --white: #ffffff;
  }
  * { box-sizing: border-box; margin: 0; padding: 0; }
  html, body { width: 900px; height: 1200px; overflow: hidden; background: var(--white); }
  body { position: relative; font-family: "Open Sans", Arial, sans-serif; color: var(--text); }

  .header-band { position: absolute; left: 24px; top: 0; width: 861px; height: 165px; background: var(--orange); }
  .portrait-frame { position: absolute; left: 84px; top: 44px; width: 162px; height: 162px; background: var(--white); border: 1px solid var(--grey-line); padding: 5px; }
  .portrait { width: 100%; height: 100%; background: linear-gradient(180deg, #b9bcc0, #a9adb2); }
  .name { position: absolute; left: 270px; top: 74px; font-family: "Fira Sans Condensed", sans-serif; font-weight: 600; font-size: 38px; color: var(--white); line-height: 1; }
  .position { position: absolute; left: 270px; top: 126px; font-family: "Fira Sans Condensed", sans-serif; font-style: italic; font-size: 18px; color: var(--orange-dark); }

  .contact { position: absolute; display: flex; align-items: center; font-style: italic; font-size: 13px; }
  .contact svg { margin-right: 12px; }
  .contact .gap { margin-left: 22px; }
  .contact-header { left: 270px; top: 174px; color: var(--orange); }
  .contact-header svg { fill: var(--orange); }

  .section-title { position: absolute; display: flex; height: 42px; border: 1px solid var(--grey-line); background: var(--white); }
  .section-title .icon { width: 47px; height: 100%; background: var(--orange); display: flex; align-items: center; justify-content: center; }
  .section-title .label { padding: 0 20px 0 18px; display: flex; align-items: center; font-family: "Fira Sans Condensed", sans-serif; font-size: 16px; color: var(--orange); }
  .title-description { left: 60px; top: 237px; }
  .title-education { left: 60px; top: 442px; }
  .title-experience { left: 488px; top: 442px; }
  .title-skills { left: 59px; top: 675px; }

  .description { position: absolute; left: 59px; top: 293px; width: 782px; font-size: 14px; line-height: 34.5px; text-align: justify; }

  .timeline { position: absolute; top: 500px; list-style: none; }
  .timeline li { height: 34.7px; font-size: 14px; display: flex; align-items: baseline; }
  .timeline .year { font-weight: 700; font-size: 20px; color: var(--navy); margin-right: 4px; }
  .education-list { left: 59px; }
  .experience-list { left: 488px; }

  .skill { position: absolute; width: 180px; text-align: center; }
  .skill h3 { font-size: 14px; font-weight: 700; color: var(--navy); letter-spacing: -0.2px; }
  .rating { display: flex; justify-content: space-between; width: 181px; margin: 14px 0 0; padding-bottom: 13px; border-bottom: 1px solid var(--grey-line); }
  .rating span { width: 12px; height: 12px; border-radius: 50%; background: var(--orange); }
  .rating span.empty { background: var(--white); border: 1px solid var(--dot-empty); }
  .skill p { font-size: 11.5px; line-height: 20px; margin-top: 12px; }

  .footer-band { position: absolute; left: 24px; top: 1126px; width: 541px; height: 74px; background: var(--footer); color: var(--white); }
  .footer-address { position: absolute; left: 64px; top: 22px; font-size: 17px; }
  .contact-footer { left: 66px; top: 52px; color: var(--white); font-size: 14px; }
  .contact-footer svg { fill: var(--white); }

  .brand { position: absolute; left: 636px; top: 1146px; display: flex; align-items: center; font-family: "Open Sans", sans-serif; font-size: 20px; letter-spacing: 1px; color: var(--footer); }
  .brand .mark { width: 14px; height: 14px; background: var(--orange); margin-right: 10px; }
</style>
</head>
<body>
  <div class="header-band"></div>
  <div class="portrait-frame"><div class="portrait" role="img" aria-label="Employee portrait photo"></div></div>
  <h1 class="name">Alexander Test</h1>
  <div class="position">Position</div>
  <div class="contact contact-header">
    <svg width="20" height="14" viewBox="0 0 20 14"><path d="M0 0h20v14H0z M2 2v10h16V2l-8 6z" fill-rule="evenodd"/><path d="M1 1l9 7 9-7"/></svg>
    <span>employee@email.com</span>
    <svg class="gap" width="16" height="18" viewBox="0 0 16 18"><path d="M3 0l4 4-2 3c1 2 3 4 5 5l3-2 3 4-3 4C7 17 0 10 0 3z"/></svg>
    <span>+ 00 00 0000</span>
  </div>

  <div class="section-title title-description">
    <div class="icon"><svg width="20" height="20" viewBox="0 0 20 20" fill="#fff"><path d="M2 14l10-10 4 4-10 10H2z M13.5 2.5l2-2 4 4-2 2z"/></svg></div>
    <div class="label">DESCRIPTION</div>
  </div>
  <p class="description">Here could be a very brief description of the particular employee. Possibly some sort of biography or other type of information. It would be best if this text box would end right here. Maximum of two lines, in my opinion. Or maybe three lines. Depending on your intentions and purpose. But I do not think it should exceed this space.</p>

  <div class="section-title title-education">
    <div class="icon"><svg width="26" height="18" viewBox="0 0 26 18" fill="#fff"><path d="M13 0l13 6-13 6L0 6z"/><path d="M5 9v5c3 3 13 3 16 0V9l-8 4z"/><path d="M23 7h1v7h-1z"/></svg></div>
    <div class="label">EDUCATION</div>
  </div>
  <ul class="timeline education-list">
    <li><span class="year">1990:</span> This is what the employee did</li>
    <li><span class="year">1995:</span> This is what the employee did</li>
    <li><span class="year">2000:</span> This is what the employee did</li>
    <li><span class="year">2010:</span> This is what the employee did</li>
  </ul>

  <div class="section-title title-experience">
    <div class="icon"><svg width="22" height="22" viewBox="0 0 22 22"><circle cx="11" cy="11" r="11" fill="#fff"/><text x="11" y="14.5" text-anchor="middle" font-family="Open Sans, sans-serif" font-size="9" font-weight="700" fill="#f27e22">XP</text></svg></div>
    <div class="label">EXPERIENCE</div>
  </div>
  <ul class="timeline experience-list">
    <li><span class="year">1996:</span> Projects he/she worked on</li>
    <li><span class="year">1999:</span> Projects he/she worked on</li>
    <li><span class="year">2000:</span> Projects he/she worked on</li>
    <li><span class="year">2010:</span> Projects he/she worked on</li>
  </ul>

  <div class="section-title title-skills">
    <div class="icon"><svg width="24" height="24" viewBox="0 0 24 24" fill="none" stroke="#fff" stroke-width="2.5"><circle cx="12" cy="12" r="7"/><path d="M12 0v5M12 19v5M0 12h5M19 12h5"/><circle cx="12" cy="12" r="2" fill="#fff" stroke="none"/></svg></div>
    <div class="label">SKILLS</div>
  </div>

  <div class="skill" style="left:57px;top:760px"><h3>SKILL 1</h3><div class="rating"><span></span><span></span><span></span><span></span><span></span><span></span><span></span><span></span><span class="empty"></span><span class="empty"></span></div><p>Here could be a description of the particular skill.</p></div>
  <div class="skill" style="left:361px;top:760px"><h3>SKILL 2</h3><div class="rating"><span></span><span></span><span></span><span></span><span></span><span></span><span></span><span></span><span class="empty"></span><span class="empty"></span></div><p>Here could be a description of the particular skill.</p></div>
  <div class="skill" style="left:661px;top:760px"><h3>SKILL 3</h3><div class="rating"><span></span><span></span><span></span><span></span><span></span><span></span><span></span><span></span><span class="empty"></span><span class="empty"></span></div><p>Here could be a description of the particular skill.</p></div>
  <div class="skill" style="left:57px;top:901px"><h3>SKILL 4</h3><div class="rating"><span></span><span></span><span></span><span></span><span></span><span></span><span></span><span></span><span class="empty"></span><span class="empty"></span></div><p>Here could be a description of the particular skill.</p></div>
  <div class="skill" style="left:361px;top:901px"><h3>SKILL 5</h3><div class="rating"><span></span><span></span><span></span><span></span><span></span><span></span><span></span><span></span><span class="empty"></span><span class="empty"></span></div><p>Here could be a description of the particular skill.</p></div>
  <div class="skill" style="left:661px;top:901px"><h3>SKILL 6</h3><div class="rating"><span></span><span></span><span></span><span></span><span></span><span></span><span></span><span></span><span class="empty"></span><span class="empty"></span></div><p>Here could be a description of the particular skill.</p></div>

  <footer class="footer-band">
    <div class="footer-address">Lindevej 12 - 2200 København N - Denmark</div>
    <div class="contact contact-footer">
      <svg width="20" height="14" viewBox="0 0 20 14"><path d="M0 0h20v14H0z M2 2v10h16V2l-8 6z" fill-rule="evenodd"/></svg>
      <span>info@solbakken-data.dk</span>
      <svg class="gap" width="16" height="18" viewBox="0 0 16 18"><path d="M3 0l4 4-2 3c1 2 3 4 5 5l3-2 3 4-3 4C7 17 0 10 0 3z"/></svg>
      <span>+45 12 34 56 78</span>
    </div>
  </footer>
  <div class="brand"><span class="mark"></span>SOLBAKKEN DATA</div>
</body>
</html>
```